Need a website setup for our new removalist business.
Our business is called Pine Harbour Removals and would like a website setup.
We don’t have a website, logo or design as of yet. Our truck is blue so something possibly that works and can incorporate the blue.

```html
<!DOCTYPE html>
<html lang="en">
<head>
<meta charset="utf-8">
<title>Pine Harbour Removals – Brand & Website</title>
<link href="https://fonts.googleapis.com/css2?family=Russo+One&family=Inter:wght@400;500;600;700&display=swap" rel="stylesheet">
<style>
:root{
  --blue:#1c4a92;
  --blue-dark:#163d7a;
  --orange:#e8582a;
  --ink:#1d2433;
  --muted:#7a808c;
  --soft:#f3f5f9;
  --board:#5a5b55;
  --white:#ffffff;
}
*{box-sizing:border-box;margin:0;padding:0}
html,body{width:1200px;height:4332px;overflow:hidden}
body{background:var(--board);font-family:"Inter",sans-serif;color:var(--ink);position:relative}
.abs{position:absolute}
.display{font-family:"Russo One",sans-serif;font-weight:400}

/* Brand board */
.brand-board{position:absolute;left:304px;top:163px;width:592px;height:376px}
.brand-main{position:absolute;left:0;top:0;width:592px;height:237px;background:var(--white);display:flex;align-items:center;justify-content:center;gap:18px}
.brand-tile{position:absolute;top:237px;width:296px;height:139px;display:flex;align-items:center;justify-content:center;gap:12px}
.brand-tile.orange{left:0;background:var(--orange)}
.brand-tile.blue{left:296px;background:var(--blue)}
.wordmark{font-family:"Russo One",sans-serif;line-height:1.05;text-transform:uppercase}
.wordmark.lg{font-size:40px;color:var(--blue)}
.wordmark.md{font-size:24px;color:var(--white)}
.mark-square{background:currentColor;flex:none}

/* Website */
.site{position:absolute;left:134px;top:686px;width:932px;height:3477px;background:var(--white);overflow:hidden}
.topbar{position:absolute;right:0;top:0;width:520px;height:22px;background:var(--blue);clip-path:polygon(14px 0,100% 0,100% 100%,0 100%);display:flex;align-items:center;justify-content:flex-end;gap:22px;padding-right:84px;color:var(--white);font-size:10px}
.topbar .socials{display:flex;gap:7px}
.topbar .socials span{width:9px;height:9px;border-radius:50%;background:var(--white);opacity:.9}
.topbar .item{display:flex;align-items:center;gap:5px}
.header-logo{position:absolute;left:84px;top:18px;display:flex;align-items:center;gap:8px;color:var(--blue)}
.header-logo .wordmark{font-size:14px;color:var(--blue)}
.nav{position:absolute;left:346px;top:42px;display:flex;gap:0;font-size:11px;font-weight:500}
.nav a{position:absolute;white-space:nowrap;color:var(--ink);text-decoration:none}
.nav a.active{color:var(--orange)}
.btn{position:absolute;display:flex;align-items:center;justify-content:center;background:var(--orange);color:var(--white);font-weight:700;font-size:11px;letter-spacing:.4px;border-radius:20px;text-transform:uppercase}

.hero{position:absolute;left:0;top:74px;width:932px;height:546px}
.hero-photo{position:absolute;inset:0;background:linear-gradient(90deg,#2a3226 0%,#3d4635 28%,#54584a 45%,#7a6a52 62%,#b69468 78%,#5a4a3c 100%)}
.hero-shade{position:absolute;inset:0;background:linear-gradient(90deg,rgba(20,24,20,.55) 0%,rgba(20,24,20,.25) 45%,rgba(0,0,0,0) 60%)}
.hero h1{position:absolute;left:84px;top:118px;color:var(--white);font-size:34px;line-height:1.2}
.hero p{position:absolute;left:84px;top:216px;width:330px;color:var(--white);font-size:13px;line-height:1.6}
.hero-curve{position:absolute;left:0;bottom:0;width:932px;height:120px}

.section-title{position:absolute;left:0;width:932px;text-align:center;font-size:26px;color:var(--ink)}
.section-title b{font-weight:400;color:var(--blue)}
.rule{position:absolute;height:3px;width:50px;background:var(--orange)}

.service{position:absolute;width:190px;text-align:center}
.service .icon{width:108px;height:108px;border-radius:50%;border:2px solid #c9d3e4;margin:0 auto;display:flex;align-items:center;justify-content:center}
.service .icon span{width:94px;height:94px;border-radius:50%;background:var(--blue)}
.service h3{font-size:12px;font-weight:600;margin-top:24px}
.service p{font-size:10.5px;color:var(--muted);line-height:1.6;margin-top:7px}
.service a{display:inline-flex;align-items:center;gap:5px;margin-top:10px;font-size:10px;font-weight:700;color:var(--orange);text-decoration:none}
.service a i{width:9px;height:9px;border-radius:50%;background:var(--orange)}

.why{position:absolute;left:0;top:1025px;width:932px;height:526px;background:var(--soft)}
.why-photo{position:absolute;left:0;top:0;width:560px;height:526px;background:linear-gradient(90deg,#e9e3da 0%,#d9d1c4 40%,#e6e4df 75%,rgba(243,245,249,0) 100%)}
.why h2{position:absolute;left:499px;top:52px;font-size:26px;line-height:1.35;color:var(--ink)}
.why h2 b{font-weight:400;color:var(--blue)}
.why-item{position:absolute;left:499px;width:380px}
.why-item svg{position:absolute;left:0;top:0}
.why-item h4{position:absolute;left:52px;top:0;font-size:12px;font-weight:600;white-space:nowrap}
.why-item p{position:absolute;left:52px;top:19px;font-size:10.5px;color:var(--muted);white-space:nowrap}

.cta{position:absolute;left:0;top:1551px;width:932px;height:560px;background:var(--blue)}
.cta h2{position:absolute;left:84px;top:72px;color:var(--white);font-size:27px;line-height:1.3}
.cta .copy{position:absolute;left:84px;top:188px;width:330px;color:#dfe6f3;font-size:10.5px;line-height:1.8}
.cta .copy p+p{margin-top:10px}
.form-card{position:absolute;left:486px;top:43px;width:359px;height:370px;background:var(--white);border-radius:8px;padding:0 16px}
.form-card h3{margin-top:46px;text-align:center;font-size:15px;color:var(--ink)}
.form-card h3 b{font-weight:400;color:var(--blue)}
.form-card .sub{text-align:center;font-size:10px;color:var(--muted);margin-top:6px}
.form-card .sub strong{color:var(--ink)}
.field{position:absolute;left:16px;width:327px;height:32px;background:var(--soft);border-radius:4px;font-size:9px;color:var(--muted);padding:11px 12px}

.step{position:absolute;width:240px;text-align:center}
.step .num{position:absolute;font-family:"Russo One",sans-serif;font-size:94px;line-height:1;color:var(--white);-webkit-text-stroke:2px #8fb4df}
.step .pic{position:absolute;width:78px;height:78px;border-radius:50%;border:3px solid #5b9bd8;background:linear-gradient(135deg,#dfe4ea,#c8a985)}
.step .dot{position:absolute;width:10px;height:10px;border-radius:50%;background:#3b8ad6}
.step h4{position:absolute;left:0;width:240px;font-size:15px;font-weight:600;line-height:1.25}

.reviews{position:absolute;left:0;top:2414px;width:932px;height:370px;background:var(--soft)}
.review{position:absolute;top:118px;width:318px;height:177px;background:var(--white);border-radius:18px;box-shadow:0 6px 18px rgba(20,40,80,.12)}
.review .avatar{position:absolute;left:-26px;top:45px;width:88px;height:88px;border-radius:50%;border:4px solid var(--white);background:linear-gradient(160deg,#b9c3cf,#5d6b7c)}
.review .quote{position:absolute;left:78px;top:12px;font-family:"Russo One",sans-serif;font-size:40px;color:var(--orange);line-height:1}
.review p{position:absolute;left:78px;top:56px;width:222px;font-size:10.5px;line-height:1.75;color:var(--muted)}
.review h5{position:absolute;left:78px;top:123px;font-size:12px;font-weight:600}
.review .stars{position:absolute;left:78px;top:140px;color:#f5a623;font-size:12px;letter-spacing:1px}
.arrow{position:absolute;top:196px}

.faq{position:absolute;left:0;top:2784px;width:932px;height:440px;background:var(--blue)}
.faq h2{position:absolute;left:0;top:52px;width:932px;text-align:center;color:var(--white);font-size:26px}
.faq-row{position:absolute;width:368px;height:34px;background:var(--white);border-radius:17px;font-size:10.5px;color:var(--ink);padding:0 18px;display:flex;align-items:center;justify-content:space-between}
.faq-row span:last-child{font-size:15px;font-weight:700}

.footer-curve{position:absolute;left:0;top:3150px;width:932px;height:90px}
.footer-logo{position:absolute;left:86px;top:3290px;display:flex;align-items:center;gap:10px;color:var(--blue)}
.footer-logo .wordmark{font-size:22px;color:var(--blue)}
.footer-social{position:absolute;left:126px;top:3366px;display:flex;gap:8px}
.footer-social span{width:24px;height:24px;border-radius:50%;border:1.5px solid #6b7280}
.fcol{position:absolute;top:3244px}
.fcol h4{font-size:12px;font-weight:600;margin-bottom:12px}
.fcol li{list-style:none;font-size:10px;color:var(--muted);line-height:20px}
.contact-line{display:flex;gap:10px;margin-bottom:10px}
.contact-line b{display:block;font-size:9px;color:var(--ink);font-weight:600}
.contact-line span{font-size:9.5px;color:var(--muted);line-height:1.5}
.divider{position:absolute;left:84px;top:3427px;width:762px;height:1px;background:#dcdfe5}
.copyright{position:absolute;left:0;top:3448px;width:932px;text-align:center;font-size:10px;color:var(--muted)}
.to-top{position:absolute;left:860px;top:3394px;width:28px;height:28px;border-radius:50%;background:var(--blue)}
</style>
</head>
<body>

<section class="brand-board" aria-label="Brand identity">
  <div class="brand-main">
    <span class="mark-square" style="width:26px;height:26px;color:var(--orange)"></span>
    <div class="wordmark lg">Pine Harbour<br>Removals</div>
  </div>
  <div class="brand-tile orange"><div class="wordmark md">Pine Harbour<br>Removals</div></div>
  <div class="brand-tile blue"><div class="wordmark md">Pine Harbour<br>Removals</div></div>
</section>

<main class="site">
  <div class="topbar">
    <div class="socials"><span></span><span></span><span></span><span></span></div>
    <div class="item">
      <svg width="10" height="8" viewBox="0 0 10 8"><rect x=".5" y=".5" width="9" height="7" rx="1" fill="none" stroke="#fff"/><path d="M.5 1 5 4.5 9.5 1" fill="none" stroke="#fff"/></svg>
      info@pineharbourremovals.com
    </div>
    <div class="item">
      <svg width="9" height="9" viewBox="0 0 24 24"><path fill="#fff" d="M6.6 10.8a15 15 0 0 0 6.6 6.6l2.2-2.2c.3-.3.7-.4 1-.2 1.1.4 2.3.6 3.6.6.6 0 1 .4 1 1V20c0 .6-.4 1-1 1A17 17 0 0 1 3 4c0-.6.4-1 1-1h3.5c.6 0 1 .4 1 1 0 1.3.2 2.5.6 3.6.1.3 0 .7-.2 1z"/></svg>
      +1 555 014 2290
    </div>
  </div>

  <div class="header-logo">
    <div class="wordmark">Pine Harbour<br>Removals</div>
  </div>
  <nav class="nav">
    <a class="active" style="left:0">Home</a>
    <a style="left:50px">Services</a>
    <a style="left:114px">Locations</a>
    <a style="left:185px">About Us</a>
    <a style="left:252px">Blog</a>
    <a style="left:294px">Contact Us</a>
  </nav>
  <a class="btn" style="left:729px;top:32px;width:116px;height:34px">Get a Quote</a>

  <section class="hero">
    <div class="hero-photo" role="img" aria-label="Removalist wheeling boxes on a trolley out of a truck, with a suburban house behind"></div>
    <div class="hero-shade"></div>
    <h1 class="display">PINE HARBOUR<br>REMOVALS</h1>
    <p>Lorem ipsum dolor sit amet, consectetur adipiscing incididunt ut labore et dolore magna aliqua.</p>
    <a class="btn" style="left:84px;top:275px;width:150px;height:40px">Get a Quote</a>
    <svg class="hero-curve" viewBox="0 0 932 120" preserveAspectRatio="none">
      <path d="M0 70 Q470 -20 932 102 L932 120 L0 120Z" fill="#fff"/>
      <path d="M380 26 Q700 14 932 96" fill="none" stroke="#e8582a" stroke-width="7"/>
    </svg>
  </section>

  <h2 class="section-title display" style="top:632px">OUR REMOVALIST <b>SERVICES</b></h2>
  <div class="rule" style="left:441px;top:673px"></div>

  <div class="service" style="left:75px;top:720px"><div class="icon"><span></span></div><h3>Local Moving</h3><p>Lorem ipsum dolor sit amet, consectetur adipiscing elit, sed ut dolore magna aliqua.</p><a>LEARN MORE <i></i></a></div>
  <div class="service" style="left:271px;top:720px"><div class="icon"><span></span></div><h3>Long-Distance Moving</h3><p>Lorem ipsum dolor sit amet, consectetur adipiscing elit, sed ut dolore magna aliqua.</p><a>LEARN MORE <i></i></a></div>
  <div class="service" style="left:468px;top:720px"><div class="icon"><span></span></div><h3>Residential Moving</h3><p>Lorem ipsum dolor sit amet, consectetur adipiscing elit, sed ut dolore magna aliqua.</p><a>LEARN MORE <i></i></a></div>
  <div class="service" style="left:664px;top:720px"><div class="icon"><span></span></div><h3>Commercial Moving</h3><p>Lorem ipsum dolor sit amet, consectetur adipiscing elit, sed ut dolore magna aliqua.</p><a>LEARN MORE <i></i></a></div>

  <section class="why">
    <div class="why-photo" role="img" aria-label="Couple sitting on the floor of a new home among moving boxes, looking at a laptop"></div>
    <h2 class="display">WHY CHOOSE PINE<br><b>HARBOUR REMOVALS</b></h2>
    <div class="rule" style="left:499px;top:136px"></div>
    <div class="why-item" style="top:176px">
      <svg width="40" height="40" viewBox="0 0 40 40" fill="none" stroke="#1c4a92" stroke-width="2"><circle cx="22" cy="22" r="13"/><path d="M22 14v8l5 4M4 16h8M2 22h8M4 28h8"/></svg>
      <h4>Fast And Detailed Quotes</h4><p>Lorem ipsum dolor sit amet, consectetur adipiscing elit do</p></div>
    <div class="why-item" style="top:238px">
      <svg width="40" height="40" viewBox="0 0 40 40" fill="none" stroke="#1c4a92" stroke-width="2"><circle cx="20" cy="12" r="7"/><path d="M8 38c0-8 5-14 12-14s12 6 12 14"/></svg>
      <h4>Trained And Professional Staff</h4><p>Lorem ipsum amet, consectetur adipiscing elit do</p></div>
    <div class="why-item" style="top:300px">
      <svg width="40" height="40" viewBox="0 0 40 40" fill="none" stroke="#1c4a92" stroke-width="2"><path d="M10 36V16l4-8 4 8v-6l4 0v10M22 20l6-10 4 2-4 12v12"/></svg>
      <h4>White Glove Moving Service</h4><p>Lorem ipsum dolor sit amet, consectetur adipiscing elit do</p></div>
    <div class="why-item" style="top:362px">
      <svg width="40" height="40" viewBox="0 0 40 40" fill="none" stroke="#1c4a92" stroke-width="2"><path d="M20 4l11 4v9c0 8-5 13-11 16C14 30 9 25 9 17V8z"/><path d="M15 18l4 4 7-7"/></svg>
      <h4>Fully Insured For Your Peace Of Mind</h4><p>Lorem ipsum amet, consectetur adipiscing elit do</p></div>
    <a class="btn" style="left:499px;top:433px;width:122px;height:34px">Learn More</a>
  </section>

  <section class="cta">
    <h2 class="display">NEED HOUSE MOVING<br>OR OFFICE RELOCATION<br>SERVICES?</h2>
    <div class="copy">
      <p>Lorem ipsum dolor sit amet, consectetur adipiscing elit, sed do eiusmod tempor incididunt ut labore et dolore magna aliqua. Ut enim ad minim veniam, quis nostrud exercitation ullamco laboris nisi ut aliquip ex ea commodo consequat.</p>
      <p>Duis aute irure dolor in reprehenderit in voluptate velit esse cillum dolore eu fugiat nulla pariatur. Excepteur sint occaecat cupidatat culpa qui officia deserunt mollit anim id est laborum.</p>
    </div>
    <a class="btn" style="left:84px;top:356px;width:150px;height:36px">Find Out More</a>

    <form class="form-card">
      <h3 class="display">READY TO MAKE <b>YOUR MOVE?</b></h3>
      <p class="sub">Call us <strong>+1 555 017 3364</strong> or Fill out the contact form below.</p>
      <div class="field" style="top:101px">Name</div>
      <div class="field" style="top:143px">Email</div>
      <div class="field" style="top:185px">Phone</div>
      <div class="field" style="top:226px">Location</div>
      <div class="field" style="top:268px;height:38px">Message</div>
      <a class="btn" style="left:16px;top:325px;width:327px;height:28px">Submit Now</a>
    </form>
  </section>

  <svg class="abs" style="left:0;top:1990px" width="932" height="130" viewBox="0 0 932 130" preserveAspectRatio="none">
    <path d="M0 110 Q330 10 932 62 L932 130 L0 130Z" fill="#fff"/>
    <path d="M0 106 Q300 14 600 32" fill="none" stroke="#e8582a" stroke-width="7"/>
  </svg>

  <h2 class="section-title display" style="top:2096px">HOW WE MAKE <b>IT HAPPEN</b></h2>
  <div class="rule" style="left:441px;top:2137px"></div>

  <svg class="abs" style="left:0;top:2170px" width="932" height="120" viewBox="0 0 932 120" fill="none">
    <path d="M226 60 Q300 20 370 55" stroke="#9aa3b2" stroke-width="1.5" stroke-dasharray="3 4"/>
    <path d="M362 48 L372 56 L360 58" stroke="#9aa3b2" stroke-width="1.5"/>
    <path d="M534 78 Q610 110 685 68" stroke="#9aa3b2" stroke-width="1.5" stroke-dasharray="3 4"/>
    <path d="M676 66 L687 68 L680 77" stroke="#9aa3b2" stroke-width="1.5"/>
  </svg>

  <div class="step" style="left:46px;top:2190px">
    <span class="num" style="left:37px;top:8px">1</span>
    <div class="pic" style="left:91px;top:12px" role="img" aria-label="Person booking a move on a phone"></div>
    <span class="dot" style="left:91px;top:14px"></span>
    <h4 style="top:115px">You Book An Order<br>With Us</h4>
  </div>
  <div class="step" style="left:345px;top:2190px">
    <span class="num" style="left:30px;top:8px">2</span>
    <div class="pic" style="left:106px;top:12px" role="img" aria-label="Packed moving boxes"></div>
    <span class="dot" style="left:106px;top:14px"></span>
    <h4 style="top:112px">We Come &amp; Pack Your<br>Home Contents</h4>
  </div>
  <div class="step" style="left:643px;top:2190px">
    <span class="num" style="left:37px;top:8px">3</span>
    <div class="pic" style="left:106px;top:12px" role="img" aria-label="Mover carrying boxes into a new home"></div>
    <span class="dot" style="left:106px;top:14px"></span>
    <h4 style="top:112px">We Drive &amp; Deliver To<br>Your New Place</h4>
  </div>

  <section class="reviews">
    <h2 class="section-title display" style="top:46px">WHAT THEY SAY <b>ABOUT US</b></h2>
    <div class="rule" style="left:441px;top:88px"></div>
    <svg class="arrow" style="left:32px" width="16" height="26" viewBox="0 0 16 26"><path d="M13 2 3 13l10 11" fill="none" stroke="#1d2433" stroke-width="3"/></svg>
    <svg class="arrow" style="left:884px" width="16" height="26" viewBox="0 0 16 26"><path d="M3 2l10 11L3 24" fill="none" stroke="#1d2433" stroke-width="3"/></svg>
    <article class="review" style="left:138px">
      <div class="avatar" role="img" aria-label="Customer portrait"></div>
      <span class="quote">“</span>
      <p>Sed ut perspiciatis unde omnis iste natus sit voluptatem accusantium doloremque laudantium, totam rem aperiam,</p>
      <h5>John Doe</h5><span class="stars">★★★★★</span>
    </article>
    <article class="review" style="left:517px">
      <div class="avatar" role="img" aria-label="Customer portrait"></div>
      <span class="quote">“</span>
      <p>Sed ut perspiciatis unde omnis iste natus sit voluptatem accusantium doloremque laudantium, totam rem aperiam,</p>
      <h5>John Doe</h5><span class="stars">★★★★★</span>
    </article>
  </section>

  <section class="faq">
    <h2 class="display">FREQUENTLY ASKED QUESTIONS</h2>
    <div class="faq-row" style="left:84px;top:131px"><span>What do removalists do?</span><span>+</span></div>
    <div class="faq-row" style="left:479px;top:131px"><span>How much do removalists cost?</span><span>+</span></div>
    <div class="faq-row" style="left:84px;top:184px"><span>How much does it cost to move an entire house?</span><span>+</span></div>
    <div class="faq-row" style="left:479px;top:184px"><span>How much does it cost to move an office?</span><span>+</span></div>
    <div class="faq-row" style="left:84px;top:238px"><span>How many boxes do I need to move?</span><span>+</span></div>
    <div class="faq-row" style="left:479px;top:238px"><span>How to choose a removalist?</span><span>+</span></div>
    <div class="faq-row" style="left:84px;top:290px"><span>What Is The Cheapest Day to Move?</span><span>+</span></div>
    <div class="faq-row" style="left:479px;top:290px"><span>Do You Pay For Removalists Upfront?</span><span>+</span></div>
  </section>

  <svg class="footer-curve" viewBox="0 0 932 90" preserveAspectRatio="none">
    <path d="M0 80 Q420 -30 932 72 L932 90 L0 90Z" fill="#fff"/>
    <path d="M300 22 Q650 10 932 70" fill="none" stroke="#e8582a" stroke-width="7"/>
  </svg>

  <footer>
    <div class="footer-logo"><div class="wordmark">Pine Harbour<br>Removals</div></div>
    <div class="footer-social"><span></span><span></span><span></span><span></span></div>

    <div class="fcol" style="left:338px">
      <h4>Quick Links</h4>
      <ul><li>Home</li><li>Services</li><li>Locations</li><li>About Us</li><li>Blog</li><li>Contact Us</li></ul>
    </div>
    <div class="fcol" style="left:480px">
      <h4>About Company</h4>
      <ul><li>Terms &amp; Conditions</li><li>Privacy Policy</li><li>Support</li><li>Site Map</li><li>FAQ</li></ul>
    </div>
    <div class="fcol" style="left:662px">
      <h4>Contact Us</h4>
      <div class="contact-line">
        <svg width="10" height="10" viewBox="0 0 24 24"><path fill="#e8582a" d="M6.6 10.8a15 15 0 0 0 6.6 6.6l2.2-2.2c.3-.3.7-.4 1-.2 1.1.4 2.3.6 3.6.6.6 0 1 .4 1 1V20c0 .6-.4 1-1 1A17 17 0 0 1 3 4c0-.6.4-1 1-1h3.5c.6 0 1 .4 1 1 0 1.3.2 2.5.6 3.6.1.3 0 .7-.2 1z"/></svg>
        <div><b>Phone</b><span>+1 (555) 014 2290</span></div>
      </div>
      <div class="contact-line">
        <svg width="10" height="10" viewBox="0 0 10 8"><rect width="10" height="8" rx="1" fill="#e8582a"/><path d="M0 1 5 4.5 10 1" fill="none" stroke="#fff"/></svg>
        <div><b>Email</b><span>hello@pineharbourremovals.com</span></div>
      </div>
      <div class="contact-line">
        <svg width="10" height="12" viewBox="0 0 24 30"><path fill="#e8582a" d="M12 0a11 11 0 0 0-11 11c0 8 11 19 11 19s11-11 11-19A11 11 0 0 0 12 0zm0 15a4 4 0 1 1 0-8 4 4 0 0 1 0 8z"/></svg>
        <div><b>Location</b><span>22 Harbour Lane,<br>Portside 40210</span></div>
      </div>
    </div>

    <div class="to-top"><svg width="28" height="28" viewBox="0 0 28 28"><path d="M9 16l5-5 5 5" fill="none" stroke="#fff" stroke-width="2"/></svg></div>
    <div class="divider"></div>
    <p class="copyright">2024 Copyright - Pine Harbour Removals | All Rights Reserved</p>
  </footer>
</main>

</body>
</html>
```